Business Card Design

we are a brand new cable TV network devoted to self improvement and leading a better life called FLOURIVO TV.I have a logo. We have 3 executives that need cards.I want it to be a heavy stock card: professional but showing our creative nature

Industry/Entity Type

Business

Contact Information for Business Card

CLAUDIA SAENZ AMLIECEO350 San Juan DrPonte Vedra Beach FL 32082904-473-5953

```html
<!DOCTYPE html>
<html lang="en">
<head>
<meta charset="utf-8">
<title>Flourivo TV Business Card</title>
<link href="https://fonts.googleapis.com/css2?family=Open+Sans:wght@400;600&family=Varela+Round&display=swap" rel="stylesheet">
<style>
  :root {
    --backdrop: #e9e6e1;
    --brand-red: #d3343c;
    --brand-red-deep: #a8242b;
    --card-white: #f7f7f7;
    --ink: #2b2b2d;
    --rule: #444446;
  }
  html, body {
    margin: 0;
    width: 1200px;
    height: 892px;
    overflow: hidden;
    background: var(--backdrop);
  }
  .card {
    position: absolute;
    left: 100px;
    top: 161px;
    width: 1000px;
    height: 570px;
    border-radius: 34px;
    overflow: hidden;
    box-shadow: 0 18px 40px rgba(0,0,0,0.18);
  }
  .card-surface {
    position: absolute;
    inset: 0;
  }
  .card-content {
    position: absolute;
    left: 150px;
    top: 118px;
    width: 720px;
    font-family: "Open Sans", sans-serif;
    color: var(--ink);
  }
  .brand-name {
    margin: 0;
    font-family: "Varela Round", sans-serif;
    font-size: 98px;
    font-weight: 400;
    line-height: 1;
    letter-spacing: -2px;
    color: var(--ink);
    white-space: nowrap;
  }
  .divider {
    height: 1px;
    background: var(--rule);
    margin: 30px 0 26px -10px;
    width: 740px;
  }
  .person-name {
    margin: 0;
    font-size: 38px;
    font-weight: 400;
    color: var(--brand-red);
    line-height: 1.1;
  }
  .person-title {
    margin: 6px 0 36px 2px;
    font-size: 21px;
  }
  .contact {
    margin: 0 0 0 2px;
    font-size: 21px;
    line-height: 1.3;
    font-style: normal;
  }
</style>
</head>
<body>
  <div class="card">
    <svg class="card-surface" viewBox="0 0 1000 570" width="1000" height="570" aria-hidden="true">
      <defs>
        <linearGradient id="band-red" x1="0" y1="0" x2="0" y2="1">
          <stop offset="0" stop-color="#d83a42"/>
          <stop offset="0.5" stop-color="#c72d35"/>
          <stop offset="1" stop-color="#a8242b"/>
        </linearGradient>
        <radialGradient id="face-white" cx="0.5" cy="0.5" r="0.7">
          <stop offset="0" stop-color="#ffffff"/>
          <stop offset="1" stop-color="#ececec"/>
        </radialGradient>
      </defs>
      <rect class="band" width="1000" height="570" fill="url(#band-red)"/>
      <path class="face" d="M0 95 Q500 -40 1000 95 L1000 475 Q500 610 0 475 Z" fill="url(#face-white)"/>
      <path class="face-edge" d="M0 95 Q500 -40 1000 95" fill="none" stroke="#1e1e1e" stroke-width="4"/>
      <path class="face-edge" d="M0 475 Q500 610 1000 475" fill="none" stroke="#1e1e1e" stroke-width="4"/>
    </svg>

    <div class="card-content">
      <h1 class="brand-name">FLOURIVO TV</h1>
      <div class="divider"></div>
      <p class="person-name">Mirella Okafor Dunst</p>
      <p class="person-title">CEO</p>
      <address class="contact">
        541-618-2047<br>
        718 Harlow Creek Dr<br>
        Larkmoor Bay OR 97381
      </address>
    </div>
  </div>
</body>
</html>
```